Web 2.0 my 1 page website ($500 Guaranteed)

Im looking for someone who can update my existing design at http://www.doriselvanby.com
I like existing layout and the way the boxes all work. Looking for the same design but with an updated web 2.0 textured look and feel.
Please note the current site is already working on top of pagecrate and new design needs to also work with pagecrate so I can continue to page content.
Looking for designer who can also get it working in pagecrate as it is today.
$500 AUD first prize for it all working.
If it helps:
I like minimailist. I like white. I like bright. I like texture. I like backgrounds. I like horizontal stripes running the length of the page. I like designs that work regardless of width of page. I like big bold statements. I like obvious. I like round edges. I like sites that look like they have come alive. I like depth. I like a 3D look. I like something very subtle that moves occassionally - just enough to catch your eye. I dont like popups. I dont like scrolling.
I like really clean SEO friendly source code. I like standards compatible design.
http://www.lotvessel.ie/ I like the depth of the mini coming out of the screen. I like the big bold fonts and the bright colours. I like the horizontal red stripe running the length of the page.
http://www.quillharbor.ie/ I like the backround clouds. I like the nice big lettering on the font on the mene bar. I like the nice bog boxes and contact numbers.
http://www.kuljepolkuja.fi/ I like the bright colours on the phone. I like the splash of the bubbles at the top of the page.
http://ontheruncue.me/ I like the blurred background. I REALLY like the rounded enter your email and notify me text boxes. I like the fonts on notify me and the textured background of the button.
http://9qtorn.com/it/ I really like the horizontal bar across the page - I like the big fonts in this background - I like the green and the orange. I really like the depth - how the beans and chair and butterfly sit on top of the page kind of bringing it to life. Like all the layers giving that illusion of 3D.
http://www.fenwrigley.net/ Like the big fonts, the horizontal bar, the leather stitching look around the "lets work together" and how everything is shadowed and sits off the page. I like the big contact us / get in touch / fonts at the bottom the big social media buttons. Probably this area could all be half the size but I like it.
http://www.drevoxis.com/ I like the graining textures in the background grays. I prefer blues and whites.
http://tibbinshedding.ca/ Like the big bold texts and the colours. Like the 3D cardboard box coming off the page.
http://pondchimers.com/ Like the textured backround - the rough grainy blue.
http://www.uk-rv.com/ I always liked those background kind of bursts behind the bay area picture in the middle. Like the striped blue background.
http://workshop.vendoqua.com/ Who doesnt like a ninja, but again like the big fonts and the way the person has depth
http://www.plumfolders.com/ I like the depth. I like the big bold colours.
http://www.5ibrelt.com/ Again like how the product is featured with lighting behind it, has that 3D look. Nice big lettering etc.
Updates
I like minimailist. I like white. I like bright. I like texture. I like
backgrounds. I like horizontal stripes running the length of the page. I
like designs that work regardless of width of page. I like big bold
statements. I like obvious. I like round edges. I like sites that look
like they have come alive. I like depth. I like a 3D look. I like
something very subtle that moves occassionally - just enough to catch
your eye. I dont like popups. I dont like scrolling.
http://www.lotvessel.ie/
I like the depth of the mini coming out of the screen. I like the big
bold fonts and the bright colours. I like the horizontal red stripe
running the length of the page.
http://www.quillharbor.ie/
I like the backround clouds. I like the nice big lettering on the font
on the mene bar. I like the nice bog boxes and contact numbers.
http://ontheruncue.me/
I like the blurred background. I REALLY like the rounded enter your
email and notify me text boxes. I like the fonts on notify me and the
textured background of the button.
http://9qtorn.com/it/
I really like the horizontal bar across the page - I like the big fonts
in this background - I like the green and the orange. I really like the
depth - how the beans and chair and butterfly sit on top of the page
kind of bringing it to life. Like all the layers giving that illusion of
3D.
http://www.fenwrigley.net/
Like the big fonts, the horizontal bar, the leather stitching look
around the "lets work together" and how everything is shadowed and sits
off the page. I like the big contact us / get in touch / fonts at the
bottom the big social media buttons. Probably this area could all be
half the size but I like it.
Typical Components of Web 2.0 Site Design
- Lots of space: Web 2.0 sites tend to have a lot of wide-open space. It's a contrast from the 90s, where the trend was to make usage of every square inch of a website's home page with links, banners and applets. White space is embraced to a major degree, as it calls attention to important buttons and links.
- The "Less Is More" Mentality: By putting less on the page, you're drawing more attention to the elements that matter: content and call-to-action buttons. "Clutter" and Web 2.0 simply do not mix - this is a new era of design psychology.
- Gradients: Merely a design element, gradients are used in Web 2.0 site design to give a clean, soft impression that's easy on the eyes.
- Large Fonts: Huge headings are a popular trend in Web 2.0 design - headings are usually taglines that describe or summarize what a website is about in just a handful of words. It's a huge benefit to first-timer usability, especially since new visitors would like to "get to the point" without having to read an intro paragraph.
- Dramatic Color Contrast: Another typical element seen in Web 2.0 design are bright colors (particularly neon colors) that accent site elements including menus, separator bars and footers. Many sites use this same neon color for their hyperlinks and headings, as well. Sometimes, the contrast between bright neon colors and charcoal or light gray text are put in unison for a dramatic effect.
- Eye Candy Logos: In Web 2.0 logo design, it's almost expected to see logos have a shiny plastic luster, or a soft gradient. Most Web 2.0 fonts are similar to basic Arial, Tahoma or Helvetica, and are simple. The colors used within the logo are also typically mimicked on other site design pieces to create a sense of uniformity.
- Huge Buttons: Calls to action (buttons that prompt you to "Get More Information," "Download Now," "See A Demo" or "Buy Now") are typically gigantic in Web 2.0 design. They're also attractive, featuring a color that strays away from the rest of the website's schematic. These buttons are typically isolated by a great deal of space, making them very easy to notice.
- Reflections: Product images, screenshots and icons can be seen as having "reflections" underneath them, as if they were standing on top of a new laminate floor. It's a stereotypical design element of Web 2.0.
- Lots of Icons: Web 2.0 icons are always in vector format, which is the standard format created by software such as Adobe Illustrator and Flash. They're attractive and clean looking, and are used to either draw attention to a website's sub-categories, a product's individual features, or anything else that the web designer wanted to help associate for a viewer.
- Exaggerated Web Form Fields: Huge form fields add to usability and draw attention to sign-ups and registrations. Instead of typing in a search, a username or anything else into a tiny web field, Web 2.0 has evolved them into massive interactive boxes with large text that makes things easy to see. For a good example, look at Glimvo.com's huge fields.

```html
<!DOCTYPE html>
<html lang="en">
<head>
<meta charset="utf-8">
<title>Doris Elvanby – Retail CIO</title>
<link rel="stylesheet" href="https://fonts.googleapis.com/css2?family=Yanone+Kaffeesatz:wght@400;600&family=Vollkorn:wght@400&family=Comfortaa:wght@400&family=Poiret+One&family=Orbitron:wght@900&family=Open+Sans:wght@700&display=swap">
<style>
:root{
  --bg-deep:#0d0b14;
  --glow-blue:rgba(120,200,235,.85);
  --glow-orange:rgba(230,120,40,.75);
  --glow-red:rgba(200,60,50,.7);
  --glow-magenta:rgba(170,20,120,.75);
  --panel:rgba(40,44,58,.72);
  --panel-front:#151219;
  --frame:#c4ccd6;
  --corner:#f2f2f2;
  --heading:#f2e43a;
  --tagline:#e6df1e;
  --link:#3fdcf2;
  --text:#ffffff;
  --follow:#d9a772;
  --badge:#fbf8dc;
  --badge-ink:#16141a;
  --social:#1f8fd6;
}
*{box-sizing:border-box;margin:0;padding:0}
html,body{width:1200px;height:1105px;overflow:hidden}
body{
  position:relative;
  background:
    radial-gradient(ellipse 260px 200px at 560px 170px,var(--glow-blue),transparent 70%),
    radial-gradient(ellipse 320px 230px at 230px 140px,var(--glow-orange),transparent 70%),
    radial-gradient(ellipse 300px 260px at 980px 120px,var(--glow-red),transparent 70%),
    radial-gradient(ellipse 420px 300px at 1150px 1000px,var(--glow-magenta),transparent 70%),
    radial-gradient(ellipse 380px 260px at 120px 620px,rgba(70,40,110,.5),transparent 70%),
    var(--bg-deep);
  font-family:"Vollkorn",Georgia,serif;
  color:var(--text);
}
a{color:var(--link);text-decoration:none}
.site-name{
  position:absolute;left:23px;top:8px;
  font-family:"Orbitron",sans-serif;font-size:58px;letter-spacing:10px;text-transform:uppercase;
  color:transparent;-webkit-text-stroke:1px rgba(220,220,230,.35);
}
.panel{
  position:absolute;background:var(--panel);border:2px solid var(--frame);
  box-shadow:0 0 14px rgba(0,0,0,.6);padding:20px 14px 14px 16px;overflow:hidden;
}
.panel::after{
  content:"";position:absolute;inset:4px;pointer-events:none;
  background:
    linear-gradient(135deg,var(--corner) 50%,transparent 50%) top left/16px 16px no-repeat,
    linear-gradient(225deg,var(--corner) 50%,transparent 50%) top right/16px 16px no-repeat,
    linear-gradient(45deg,var(--corner) 50%,transparent 50%) bottom left/16px 16px no-repeat,
    linear-gradient(315deg,var(--corner) 50%,transparent 50%) bottom right/16px 16px no-repeat;
}
.panel h2{font-family:"Yanone Kaffeesatz",sans-serif;font-weight:400;color:var(--heading);font-size:19px;margin-bottom:10px}
.panel p{font-size:13px;line-height:15px;color:rgba(255,255,255,.45);margin-bottom:12px}
.panel p a{color:rgba(63,220,242,.5)}
.panel-travel{left:75px;top:159px;width:431px;height:300px}
.panel-tweets{left:425px;top:218px;width:489px;height:392px}
.panel-career{left:21px;top:311px;width:495px;height:266px}
.panel-interests{left:431px;top:342px;width:483px;height:268px}
.panel-welcome{
  left:53px;top:420px;width:736px;height:410px;background:var(--panel-front);
  padding:30px 24px 20px 17px;box-shadow:0 0 18px rgba(0,0,0,.8),0 4px 0 -2px rgba(230,220,40,.5);
}
.panel-welcome h2{font-size:32px;font-weight:600;margin-bottom:12px}
.panel-welcome p{font-size:16.3px;line-height:20px;color:var(--text);margin-bottom:22px}
.panel-welcome p a{color:var(--link)}
.portrait{
  position:absolute;left:808px;top:70px;width:375px;height:380px;
  background:radial-gradient(ellipse 120px 90px at 50% 20%,#b58667,transparent 75%),
    linear-gradient(180deg,#2a2226 0%,#141215 55%,#0c0b0d 100%);
  border-radius:50% 50% 12px 12px/30% 30% 12px 12px;
}
.badge{
  position:absolute;left:834px;top:401px;width:330px;height:159px;background:var(--badge);
  border-radius:18px;box-shadow:0 0 10px rgba(0,0,0,.6);
}
.badge-mark{position:absolute;left:16px;top:14px;width:54px;height:54px;border-radius:50%;background:var(--badge-ink)}
.badge-name{position:absolute;right:22px;top:44px;font-family:"Yanone Kaffeesatz",sans-serif;font-weight:600;font-size:44px;color:var(--badge-ink);white-space:nowrap}
.badge-role{position:absolute;right:22px;top:104px;font-family:"Yanone Kaffeesatz",sans-serif;font-weight:600;font-size:30px;color:var(--badge-ink)}
.follow{position:absolute;left:822px;top:704px;width:370px;display:flex;align-items:center;gap:14px;white-space:nowrap}
.follow-label{font-family:"Poiret One",sans-serif;font-size:32px;line-height:40px;color:var(--follow);letter-spacing:1px;margin-right:2px}
.social{display:flex;align-items:center;gap:6px;font-family:"Yanone Kaffeesatz",sans-serif;font-size:20px;color:var(--text)}
.social i{display:block;width:20px;height:20px;background:var(--social);border-radius:4px}
.tagline{
  position:absolute;left:37px;top:862px;width:1140px;
  font-family:"Comfortaa",sans-serif;font-size:35px;line-height:35px;color:var(--tagline);
}
.footer{
  position:absolute;left:0;right:0;top:1008px;border-top:1px solid rgba(255,255,255,.12);
  padding-top:12px;text-align:center;font-family:"Open Sans",sans-serif;font-size:13px;color:var(--text);
}
</style>
</head>
<body>
<div class="site-name">Doris Elvanby</div>

<section class="panel panel-travel">
  <h2>Travelling Australia</h2>
  <p>Hello, and welcome to my home page on the web. There isn't really much going on here, more just a front end for my webmail etc. For those that are interested in learning a bit more about me <a href="#">personally</a> or <a href="#">commercially</a>, feel free to click around and have a look.</p>
  <p>My background is basically a sales guy who a long time ago learnt how to use technology to reach the masses. After running <a href="#">BBS's</a> for years to support our computer business, I built my first commercial web site around 1994.</p>
</section>

<section class="panel panel-tweets">
  <h2>Tweets</h2>
  <p>Hello, and welcome to my home page on the web. There isn't really much going on here, more just a front end for my webmail etc. For those that are interested in learning a bit more about me <a href="#">personally</a> or <a href="#">commercially</a>, feel free to click around and have a look.</p>
  <p>My background is basically a sales guy who a long time ago learnt how to use technology to reach the masses. After running BBS's for years to support our computer business, I built my first commercial web site around 1994 and quickly moved into full blown eCommerce sites.</p>
</section>

<section class="panel panel-career">
  <h2>Career Timelin</h2>
  <p>Hello, and welcome to my home page on the web. There isn't really much going on here, more just a front end for my webmail etc. For those that are interested in learning a bit more about me <a href="#">personally</a> or <a href="#">commercially</a>, feel free to click around and have a look.</p>
  <p>My background is basically a sales guy who a long time ago learnt how to use technology to reach the masses.</p>
</section>

<section class="panel panel-interests">
  <h2>Current Interests</h2>
  <p>Hello, and welcome to my home page on the web. There isn't really much going on here, more just a front end for my webmail etc. For those that are interested in learning a bit more about me personally or commercially.</p>
  <p>In 2007 I went back into mainstream retail as the CIO of <a href="#">Marlow Bean Coffees</a>. In 2010 looking for a new challenge I joined <a href="#">Corvane</a>.</p>
</section>

<section class="panel panel-welcome">
  <h2>Welcome</h2>
  <p>Hello, and welcome to my home page on the web. There isn't really much going on here, more just a front end for my webmail etc. For those that are interested in learning a bit more about me <a href="#">personally</a> or <a href="#">commercially</a>, feel free to click around and have a look.</p>
  <p>My background is basically a sales guy who a long time ago learnt how to use technology to reach the masses. After running <a href="#">BBS's</a> for years to support our computer business, I built my first commercial web site around 1994 and quickly moved into full blown <a href="#">eCommerce</a> sites. Did a stint next in <a href="#">Web Marketing</a> and <a href="#">SEO</a> which lead to a couple of years of hammering<br><a href="#">affiliate programs</a> and <a href="#">Querio Adspace</a> across the web.</p>
  <p style="margin-top:34px">In 2007 I went back into mainstream retail as the <a href="#">CIO</a> of <a href="#">Marlow Bean Coffees</a><br>one of Australias largest franchises. In 2010 looking for a new challenge I joined <a href="#">Corvane</a><br>in their newly created role as head of Retail Technology.</p>
</section>

<div class="portrait" role="img" aria-label="Portrait photo of Doris Elvanby in a dark shirt"></div>

<div class="badge">
  <span class="badge-mark"></span>
  <span class="badge-name">Doris Elvanby</span>
  <span class="badge-role">RETAIL CIO</span>
</div>

<nav class="follow">
  <span class="follow-label">FOLLOW ME</span>
  <a class="social" href="#"><i></i>Chirpa</a>
  <a class="social" href="#"><i></i>Netlink</a>
</nav>

<p class="tagline">Retail CIO with a passion for multi - channel, multi-store technology. Specialise in using online communications to help drive the business by consumer engagements.</p>

<footer class="footer">© 2011, All Rights Reserved, Doris Elvanby</footer>
</body>
</html>
```